Buch-Cover für Sonnenherz gesucht
Der Designer hat sich sehr schnell in meine Vorgaben eingearbeitet und gleichzeitig wertvolle Vorschläge zur Optimierung abgegeben. Das Ergebnis ist dadurch sogar besser geworden, als ich mir im Vorfeld ausgemalt hatte. 100% Weiterempfehlung.
Zielgruppe
Wir sind eine Firma die hochwertige Fitnessprodukte produziert und vertreibt. Unsere Zielgruppe sind gesundheitsbewusste Frauen ab Mitte 20 bis open end, die hohe Ansprüche an sich selbst stellen und sich für das Thema Selbstoptimierung interessieren.
Aufgabenstellung
Es soll ein Hardcover gestaltet werden.
Buchtitel: Sonnenherz, Untertitel: Das Erwachen der Seele
Detaillierte Beschreibung der Projektanforderungen siehe Anhang Projektbeschreibung. Darüber hinaus bin ich auch für alternative Gestaltungs-Ideen offen.
Das Design soll der Käuferin folgendes vermitteln:
- Wertigkeit
- Positivität
und sie ein bisschen träumen lassen und natürlich neugierig auf den Inhalt machen.

```html
<!DOCTYPE html>
<html lang="de">
<head>
<meta charset="utf-8">
<title>Sonnenherz – Buchumschlag</title>
<link rel="stylesheet" href="https://fonts.googleapis.com/css2?family=Cinzel:wght@500;600&family=EB+Garamond:wght@400&family=Encode+Sans+Semi+Condensed:wght@300&family=Marcellus&family=Sacramento&display=swap">
<style>
  :root {
    --orange: #f2661a;
    --orange-light: #f8b545;
    --spine: #f5a431;
    --ink: #2a1f14;
    --panel: rgba(255, 255, 255, 0.62);
    --white: #ffffff;
  }
  * { margin: 0; padding: 0; box-sizing: border-box; }
  html, body { width: 1200px; height: 894px; overflow: hidden; background: #fff; }
  .cover {
    position: relative;
    width: 1200px;
    height: 894px;
    overflow: hidden;
  }
  .cover-photo {
    position: absolute;
    inset: 0;
    background:
      radial-gradient(ellipse 180px 120px at 900px 160px, rgba(255,238,190,0.7), transparent 70%),
      radial-gradient(ellipse 260px 200px at 930px 460px, rgba(214,170,100,0.6), transparent 70%),
      radial-gradient(ellipse 140px 260px at 1060px 520px, rgba(232,200,150,0.55), transparent 70%),
      radial-gradient(ellipse 300px 200px at 250px 80px, rgba(250,232,190,0.7), transparent 70%),
      radial-gradient(ellipse 300px 220px at 200px 820px, rgba(120,80,40,0.6), transparent 70%),
      radial-gradient(ellipse 260px 180px at 880px 840px, rgba(110,75,40,0.6), transparent 70%),
      linear-gradient(180deg, #d9b57c 0%, #b88a4f 35%, #8e6438 65%, #6b4a2a 100%);
  }
  .back-panel {
    position: absolute;
    left: 57px; top: 77px;
    width: 479px; height: 624px;
    background: var(--panel);
  }
  .back-heading {
    position: absolute;
    left: 57px; top: 110px; width: 479px;
    text-align: center;
    font-family: "Encode Sans Semi Condensed", sans-serif;
    font-weight: 300;
    font-size: 41px;
    letter-spacing: -0.5px;
    color: var(--orange);
  }
  .blurb {
    position: absolute;
    left: 68px; top: 183px; width: 460px;
    font-family: "EB Garamond", serif;
    font-size: 18.6px;
    line-height: 21.9px;
    color: var(--ink);
  }
  .blurb p + p { margin-top: 21.9px; }
  .isbn-box {
    position: absolute;
    left: 311px; top: 723px;
    width: 217px; height: 130px;
    background: var(--white);
  }
  .spine {
    position: absolute;
    left: 553px; top: 0;
    width: 90px; height: 894px;
    background: var(--spine);
  }
  .spine-imprint {
    position: absolute;
    left: 0; top: 52px; width: 90px;
    display: flex; flex-direction: column; align-items: center; gap: 4px;
    font-family: "Cinzel", serif; font-weight: 600;
    font-size: 11px; color: var(--white);
  }
  .spine-imprint .dot { width: 16px; height: 16px; border-radius: 50%; background: var(--white); }
  .spine-title {
    position: absolute;
    left: 0; top: 262px; width: 90px; height: 290px;
    writing-mode: vertical-rl;
    display: flex; align-items: center; justify-content: center;
    font-family: "Encode Sans Semi Condensed", sans-serif; font-weight: 300;
    font-size: 54px; letter-spacing: -1px; line-height: 1;
    color: var(--white);
  }
  .spine-author {
    position: absolute;
    left: 0; top: 690px; width: 90px; height: 172px;
    writing-mode: vertical-rl;
    display: flex; align-items: center; justify-content: center;
    font-family: "Cinzel", serif; font-weight: 500;
    font-size: 19px; color: var(--white);
  }
  .front-author {
    position: absolute;
    left: 643px; top: 40px; width: 557px;
    text-align: center;
    font-family: "Cinzel", serif; font-weight: 600;
    font-size: 21px; color: var(--ink);
  }
  .front-title, .front-subtitle { position: absolute; left: 643px; top: 0; }
</style>
</head>
<body>
<main class="cover">
  <div class="cover-photo" role="img" aria-label="Unscharfes, sonnig-goldenes Foto: Blick aus einem Cabrio auf eine Landstraße, eine blonde Frau mit Sonnenbrille am Steuer, Lichtreflexe"></div>

  <section class="back">
    <div class="back-panel"></div>
    <h2 class="back-heading">WAS ZÄHLT WIRKLICH?</h2>
    <div class="blurb">
      <p>Ich habe mich oft gefragt: Wie soll ich bloß die Liebe und Bestätigung, die mir damals in meiner Kindheit verwehrt blieben, „nachholen“? Lösungsansätze für mein Problem hatte ich in der Vergangenheit durchaus: Ich versuchte das Loch in mir mit Hilfe zur Selbsthilfe, Erfolg im Job und Konsum zu stopfen. Und meine Partner mussten auch für so einiges herhalten.</p>
      <p>Von Gott wollte ich lange nichts wissen. Schließlich hatte er es zugelassen, dass mir sehr viel Unheil in meinem Leben widerfahren ist. Und deshalb war ich echt wütend auf ihn.</p>
      <p>Heutzutage bin ich mir sicher, dass ich mit dieser Denkweise meine Lebenszeit verschwendet habe. Letzten Sommer begriff ich endlich: im Leben gilt die gleiche Gesetzmäßigkeit wie beim Autofahren. Der Rückspiegel ist so klein und die Frontscheibe so groß, weil das, was vor uns liegt, viel wichtiger ist als das, was hinter uns liegt. Aufgrund dieser Erkenntnis entschied ich mich, einen völlig neuen Weg einzuschlagen und wagte mich auf eine spannende Reise, die mein Leben für immer veränderte …</p>
    </div>
    <div class="isbn-box"></div>
  </section>

  <section class="spine">
    <div class="spine-imprint"><span class="dot"></span><span>Lichtweg</span></div>
    <div class="spine-title">SONNENHERZ</div>
    <div class="spine-author">Mara Feltkamp</div>
  </section>

  <section class="front">
    <p class="front-author">Mara Feltkamp</p>
    <svg class="front-title" width="557" height="300" viewBox="0 0 557 300" aria-label="Sonnenherz">
      <text x="278" y="235" text-anchor="middle" textLength="500" lengthAdjust="spacingAndGlyphs"
            font-family="Sacramento, cursive" font-size="190"
            fill="var(--orange)" stroke="var(--orange-light)" stroke-width="5" paint-order="stroke">Sonnenherz</text>
    </svg>
    <svg class="front-subtitle" width="557" height="894" viewBox="0 0 557 894" aria-label="Das Erwachen der Seele">
      <text x="275" y="764" text-anchor="middle" textLength="456" lengthAdjust="spacingAndGlyphs"
            font-family="Marcellus, serif" fill="var(--orange)">
        <tspan font-size="36">DAS </tspan><tspan font-size="60">ERWACHEN</tspan>
      </text>
      <text x="278" y="844" text-anchor="middle" textLength="240" lengthAdjust="spacingAndGlyphs"
            font-family="Marcellus, serif" fill="var(--orange)">
        <tspan font-size="36">DER </tspan><tspan font-size="62">SEELE</tspan>
      </text>
    </svg>
  </section>
</main>
</body>
</html>
```